Larchmoor Farm Brochure

To design a small brochure that tells people about our U-Pick cherry farm, where we are, when we are open and what our contact details are.

We have existing logo's which should be used. I have uploaded a file with these details.

Details about us are all located on:-
www.huddlepage.net/larchmoorfarm
https://circles.quorvane.net/u/0/b/570918346627304519837/570918346627304519837/about/p/pub

Farm

```html
<!DOCTYPE html>
<html lang="en">
<head>
<meta charset="utf-8">
<title>Larchmoor Farm Brochure</title>
<link href="https://fonts.googleapis.com/css2?family=Lato:wght@300;400;700&display=swap" rel="stylesheet">
<style>
:root{
  --bg-top:#f2f2f2;
  --bg-bottom:#d9d9d9;
  --paper:#ffffff;
  --brand-green:#3f9a3a;
  --lime:#9cc320;
  --lime-light:#d4e36a;
  --deep-green:#1f7a4a;
  --mid-green:#5aa84a;
  --wine:#7a2a22;
  --purple:#7a3a9a;
  --sky:#bfe3f5;
  --sun:#f3e27a;
  --ink:#444444;
  --soft-ink:#666666;
}
*{box-sizing:border-box;margin:0;padding:0}
html,body{width:1200px;height:900px;overflow:hidden}
body{
  background:linear-gradient(180deg,var(--bg-top),var(--bg-bottom));
  font-family:'Lato',sans-serif;color:var(--ink);position:relative;
}
.brochure{
  position:absolute;left:320px;top:50px;width:560px;height:800px;
  background:var(--paper);box-shadow:0 10px 30px rgba(0,0,0,.18);overflow:hidden;
}
.brand{
  position:absolute;left:26px;top:26px;display:flex;align-items:center;gap:8px;
  color:var(--brand-green);font-weight:700;font-size:28px;line-height:1;
}
.brand-dot{width:12px;height:12px;border-radius:50%;background:var(--lime)}
.hero{position:absolute;left:0;top:0}
.bar{
  position:absolute;top:560px;height:36px;background:linear-gradient(90deg,var(--lime),#7fb52a);
  color:#fff;font-size:19px;font-weight:300;display:flex;align-items:center;
}
.bar-who{left:28px;width:190px;border-radius:18px 0 0 18px;padding-left:24px}
.bar-value{left:342px;width:190px;border-radius:0 18px 18px 0;justify-content:flex-end;padding-right:24px}
.timings{
  position:absolute;left:200px;top:530px;width:164px;height:216px;border-radius:22px;
  background:linear-gradient(180deg,var(--lime) 0%,var(--mid-green) 45%,var(--deep-green) 100%);
  color:#fff;padding:20px 10px;
}
.timings-title{
  border:1.5px solid #fff;border-radius:16px;text-align:center;font-size:17px;font-weight:300;
  padding:4px 0;margin-bottom:24px;
}
.timings-row{display:flex;align-items:center;gap:6px;font-size:8.2px;margin-bottom:22px;white-space:nowrap}
.timings-row b{font-weight:700;margin-right:4px}
.chev{width:18px;height:14px;flex:none}
.column{
  position:absolute;top:606px;font-size:6.6px;line-height:1.35;color:var(--soft-ink);text-align:justify;
}
.column p{margin-bottom:4px}
.column-left{left:28px;width:166px}
.column-right{left:370px;width:162px}
.footer-brand{
  position:absolute;left:0;width:560px;top:756px;text-align:center;
  color:var(--brand-green);font-weight:700;font-size:22px;
}
.contact{position:absolute;left:28px;top:760px;font-size:8.5px;color:var(--soft-ink)}
.contact-row{display:flex;align-items:center;gap:6px;margin-bottom:7px}
.contact-row svg{width:11px;height:11px}
.call{position:absolute;right:28px;top:750px;text-align:right;color:var(--soft-ink)}
.call-label{font-size:10px}
.call-number{font-size:22px;font-weight:400;color:#555}
</style>
</head>
<body>
<main class="brochure">
  <svg class="hero" width="560" height="540" viewBox="0 0 560 540">
    <defs>
      <radialGradient id="pearl" cx="45%" cy="40%" r="65%">
        <stop offset="0" stop-color="#ffffff"/><stop offset="1" stop-color="#dcdcdc"/>
      </radialGradient>
      <linearGradient id="leafy" x1="0" y1="0" x2="0" y2="1">
        <stop offset="0" stop-color="#8fc23a"/><stop offset="1" stop-color="#1f7a4a"/>
      </linearGradient>
      <linearGradient id="orchard" x1="0" y1="0" x2="0" y2="1">
        <stop offset="0" stop-color="#4f8a34"/><stop offset="1" stop-color="#2d5a22"/>
      </linearGradient>
    </defs>
    <circle cx="210" cy="200" r="160" fill="none" stroke="#e2e2e2" stroke-width="1"/>
    <circle cx="265" cy="95" r="78" fill="var(--lime-light)"/>
    <circle cx="190" cy="100" r="16" fill="var(--sun)"/>
    <circle cx="395" cy="100" r="22" fill="var(--sky)"/>
    <circle cx="380" cy="300" r="158" fill="var(--wine)"/>
    <circle cx="270" cy="400" r="88" fill="var(--purple)"/>
    <circle cx="315" cy="480" r="44" fill="var(--sun)"/>
    <circle cx="480" cy="300" r="14" fill="var(--lime-light)"/>
    <circle cx="480" cy="440" r="28" fill="var(--sun)"/>
    <circle cx="520" cy="220" r="12" fill="var(--sky)"/>
    <circle cx="85" cy="400" r="16" fill="var(--purple)"/>
    <circle cx="460" cy="480" r="7" fill="var(--lime-light)"/>
    <circle cx="505" cy="370" r="4" fill="#e05a5a"/>
    <circle cx="205" cy="205" r="132" fill="url(#pearl)"/>
    <rect x="110" y="170" width="190" height="80" rx="20" fill="#e8ece8" role="img" aria-label="Photo of the white farm delivery van"/>
    <circle cx="405" cy="195" r="62" fill="url(#orchard)" role="img" aria-label="Photo of a picker among cherry tree leaves"/>
    <circle cx="175" cy="470" r="68" fill="url(#orchard)" role="img" aria-label="Photo of a picker beside a laden cherry tree"/>
    <circle cx="380" cy="380" r="100" fill="url(#leafy)"/>
    <g fill="#fff" text-anchor="middle" font-family="Lato, sans-serif">
      <text x="380" y="350" font-size="21" font-weight="300">HAPPY TREES</text>
      <text x="380" y="372" font-size="11.5" font-weight="400">THAT'S WHAT MAKES OUR</text>
      <text x="380" y="405" font-size="31" font-weight="700">CHERRIES</text>
      <text x="380" y="425" font-size="11.5" font-weight="300">JUICIER AND SWEETER</text>
    </g>
  </svg>

  <div class="brand"><span class="brand-dot"></span><span>Larchmoor<br>Farm</span></div>

  <div class="bar bar-who">Who We Are?</div>
  <div class="bar bar-value">We Value!</div>

  <section class="timings">
    <div class="timings-title">Our Timings</div>
    <div class="timings-row"><svg class="chev" viewBox="0 0 18 14"><path d="M2 2l5 5-5 5M9 2l5 5-5 5" fill="none" stroke="#fff" stroke-width="2.4"/></svg><span><b>Sunday</b>10:00 am – 5:00 pm</span></div>
    <div class="timings-row"><svg class="chev" viewBox="0 0 18 14"><path d="M2 2l5 5-5 5M9 2l5 5-5 5" fill="none" stroke="#fff" stroke-width="2.4"/></svg><span><b>Friday</b>10:00 am – 5:00 pm</span></div>
    <div class="timings-row"><svg class="chev" viewBox="0 0 18 14"><path d="M2 2l5 5-5 5M9 2l5 5-5 5" fill="none" stroke="#fff" stroke-width="2.4"/></svg><span><b>Saturday</b>10:00 am – 5:00 pm</span></div>
  </section>

  <div class="column column-left">
    <p>Larchmoor Farm is in the beautiful Yarra Valley, an ideal location for growing sweet juicy cherries. Visit us for Pick Your Own or Pre-Picked Cherries.</p>
    <p>When picking, you can eat as much as you want. Take away U-Pick fruit is $8 per kilo. There are no entry fees.</p>
    <p>Visitors are welcome to picnic beside our scenic dam and enjoy views of the valley and distant ranges.</p>
    <p>Farmer Ellis can show you how to pick, where the best cherries are that day, and the organic principles we use on our trees.</p>
    <p>Cherries have grown here for some 50 years, and some trees date back to the first plantings.</p>
  </div>

  <div class="column column-right">
    <p>We have 12 varieties of cherries, most of them heritage kinds rarely found elsewhere. Some have near black fruit, some bright red skins and others firm flesh. Our cherries ripen from mid November until early January.</p>
    <p>Larchmoor Farm was run by two generations of the Corlett Family, long respected growers in the valley.</p>
    <p>Farmer Ellis is a third generation farmer who worked in orchards across the state before taking on Larchmoor.</p>
  </div>

  <div class="footer-brand">Larchmoor Farm</div>

  <div class="contact">
    <div class="contact-row"><svg viewBox="0 0 12 12"><circle cx="6" cy="6" r="5" fill="none" stroke="#888"/><path d="M1 6h10M6 1c-2.5 3-2.5 7 0 10M6 1c2.5 3 2.5 7 0 10" fill="none" stroke="#888" stroke-width=".8"/></svg>www.larchmoorfarm.com.au</div>
    <div class="contact-row"><svg viewBox="0 0 12 12"><rect x="1" y="2.5" width="10" height="7" fill="none" stroke="#888"/><path d="M1 2.5l5 4 5-4" fill="none" stroke="#888"/></svg>ellis@hartwellph.com.au</div>
  </div>

  <div class="call">
    <div class="call-label">Call Us For More Info!</div>
    <div class="call-number">1300 555 214</div>
  </div>
</main>
</body>
</html>
```